Looking for something outstanding

2 side business card, one side just the logo preferably the metallic 3D color or my original logo for uv printing. Be creative

Colors

Designer to choose colors to be used in the design.

Requirements
Must have
• Here my info for the business cards
• Owen Hardy
• President
• (555) 302-8816
• Owen@cobaltbuildgroup.com
• Office@cobaltbuildgroup.com
• www.cobaltbuildgroup.com
• FB @cobaltbuildgroup
• Dallas-Fort Worth

```html
<!DOCTYPE html>
<html lang="en">
<head>
<meta charset="utf-8">
<title>Cobalt Build Group – Business Card</title>
<link rel="stylesheet" href="https://fonts.googleapis.com/css2?family=Montserrat:wght@500;600;700&family=Roboto:wght@400;700&display=swap">
<style>
  :root {
    --bg: #d4d4d2;
    --card-white: #f5f5f5;
    --card-black: #1b1b1b;
    --brand-red: #e3151f;
    --brand-blue: #2f44a0;
    --ink: #3a3a3a;
    --silver: #9a9a9a;
  }
  * { margin: 0; padding: 0; box-sizing: border-box; }
  html, body { width: 1200px; height: 811px; overflow: hidden; }
  body {
    background: var(--bg);
    display: flex;
    align-items: center;
    justify-content: center;
    gap: 30px;
    font-family: "Roboto", sans-serif;
  }
  .card {
    position: relative;
    width: 560px;
    height: 320px;
    box-shadow: 0 6px 18px rgba(0,0,0,0.18);
    overflow: hidden;
  }
  .card-front { background: var(--card-white); }
  .card-back { background: var(--card-black); display: flex; align-items: center; justify-content: center; }

  .brand {
    display: flex;
    align-items: center;
    gap: 10px;
    font-family: "Montserrat", sans-serif;
    font-weight: 700;
    letter-spacing: 0.06em;
    white-space: nowrap;
  }
  .brand-mark { width: 14px; height: 14px; border-radius: 50%; flex: none; }
  .card-front .brand { position: absolute; left: 30px; top: 36px; font-size: 26px; color: var(--brand-red); }
  .card-front .brand-mark { background: var(--brand-red); }
  .card-back .brand { font-size: 34px; color: var(--silver); }
  .card-back .brand-mark { width: 18px; height: 18px; border-radius: 0; background: var(--silver); }

  .side-tab { position: absolute; right: 0; top: 22px; width: 9px; height: 34px; background: var(--brand-red); }

  .person-name {
    position: absolute; right: 36px; top: 84px;
    font-weight: 700; font-size: 20px; color: var(--brand-red); letter-spacing: 0.01em;
  }
  .person-title { position: absolute; right: 36px; top: 120px; font-size: 13px; color: var(--ink); }

  .rule { position: absolute; left: 30px; right: 112px; top: 114px; height: 1.5px; background: var(--brand-red); }

  .address { position: absolute; left: 60px; top: 140px; font-style: normal; font-size: 14px; line-height: 1.35; color: var(--ink); }
  .contacts { position: absolute; left: 60px; top: 192px; list-style: none; font-size: 14px; line-height: 1.4; color: var(--ink); }
  .contacts li { display: flex; align-items: center; gap: 8px; white-space: nowrap; }
  .contacts svg { width: 12px; height: 12px; flex: none; }
</style>
</head>
<body>
  <section class="card card-front">
    <div class="brand"><span class="brand-mark"></span>COBALT BUILD GROUP</div>
    <span class="side-tab"></span>
    <div class="person-name">OWEN HARDY</div>
    <div class="person-title">President</div>
    <div class="rule"></div>
    <address class="address">
      P.O. Box: 4410, Commerce Street<br>
      Dallas-Fort Worth, Texas
    </address>
    <ul class="contacts">
      <li>
        <svg viewBox="0 0 12 12" aria-hidden="true"><circle cx="6" cy="6" r="6" fill="var(--brand-red)"/><path d="M4 3.2l1 1.4-.6.7c.4.8 1 1.4 1.8 1.8l.7-.6 1.4 1-.6 1.1C5.6 8.5 3.5 6.4 3.3 3.8z" fill="#fff"/></svg>
        (555) 302-8816
      </li>
      <li>
        <svg viewBox="0 0 12 12" aria-hidden="true"><rect x="0" y="2" width="12" height="8" fill="var(--brand-blue)"/><path d="M0.5 2.5L6 6.5l5.5-4" stroke="#fff" fill="none" stroke-width="0.9"/></svg>
        Owen@cobaltbuildgroup.com
      </li>
      <li>
        <svg viewBox="0 0 12 12" aria-hidden="true"><rect x="0" y="2" width="12" height="8" fill="var(--brand-blue)"/><path d="M0.5 2.5L6 6.5l5.5-4" stroke="#fff" fill="none" stroke-width="0.9"/></svg>
        Office@cobaltbuildgroup.com
      </li>
      <li>
        <svg viewBox="0 0 12 12" aria-hidden="true"><circle cx="6" cy="6" r="6" fill="var(--brand-red)"/><circle cx="6" cy="6" r="3.6" fill="none" stroke="#fff" stroke-width="0.9"/><path d="M2.4 6h7.2M6 2.4v7.2" stroke="#fff" stroke-width="0.9"/></svg>
        www.cobaltbuildgroup.com
      </li>
      <li>
        <svg viewBox="0 0 12 12" aria-hidden="true"><circle cx="6" cy="6" r="6" fill="var(--brand-blue)"/></svg>
        FB @cobaltbuildgroup
      </li>
    </ul>
  </section>

  <section class="card card-back">
    <div class="brand"><span class="brand-mark"></span>COBALT BUILD GROUP</div>
  </section>
</body>
</html>
```